Business Card for Dental Surgery

Professional and vibrant business card for dental surgery

Other side to incorporate space for appointment date and times

My website is www.tallowbydental.com.au

Target Market(s)

All

Industry/Entity Type

Dental

Requirements
Must have
• Catchy
Phone no, internet etc
Nice to have
• portray same image as website.
on reverse appointment side:
"Please give 24 hours notice if you cannot attend"
Nice colours

```html
<!DOCTYPE html>
<html lang="en">
<head>
<meta charset="utf-8">
<title>Tallowby Dental – Business Card</title>
<link rel="stylesheet" href="https://fonts.googleapis.com/css2?family=Open+Sans:wght@400;600&display=swap">
<style>
  :root {
    --purple: #a65ba6;
    --grey: #7f8083;
    --green: #abcd6d;
    --white: #ffffff;
  }
  html, body {
    margin: 0;
    padding: 0;
    width: 1200px;
    height: 686px;
    overflow: hidden;
    background: var(--white);
  }
  .card {
    position: relative;
    width: 1200px;
    height: 686px;
    background: var(--white);
    font-family: "Open Sans", sans-serif;
    overflow: hidden;
  }
  .practice-title {
    position: absolute;
    left: 28px;
    top: 18px;
    margin: 0;
    color: var(--purple);
    font-size: 116px;
    font-weight: 600;
    line-height: 150px;
    letter-spacing: -1px;
    white-space: nowrap;
  }
  .dentists {
    position: absolute;
    left: 748px;
    top: 204px;
    margin: 0;
    padding: 0;
    list-style: none;
    color: var(--grey);
    font-size: 35px;
    line-height: 46px;
    letter-spacing: 0.8px;
    white-space: nowrap;
  }
  .dentists .credentials {
    font-size: 18px;
    letter-spacing: 0.5px;
    margin-left: 6px;
  }
  .band {
    position: absolute;
    left: 0;
    top: 380px;
    width: 1200px;
    height: 306px;
  }
  .band path { fill: var(--green); }
  .contact {
    position: absolute;
    top: 468px;
    margin: 0;
    color: var(--white);
    font-size: 33px;
    line-height: 54px;
    letter-spacing: 1.2px;
    font-style: normal;
    white-space: nowrap;
  }
  .contact-address { left: 80px; }
  .contact-address .practice-name { font-size: 41px; letter-spacing: 1.5px; }
  .contact-lines { left: 587px; }
  .contact span { display: block; }
</style>
</head>
<body>
  <div class="card">
    <h1 class="practice-title">Tallowby Dental</h1>

    <ul class="dentists">
      <li>Dr. Martin Hale <span class="credentials">BDS</span></li>
      <li>Dr. Colin Marsh <span class="credentials">BDS FRACDS</span></li>
    </ul>

    <svg class="band" viewBox="0 0 1200 306" preserveAspectRatio="none" aria-hidden="true">
      <path d="M0 14 C 80 10, 140 8, 220 10 C 340 14, 440 20, 520 32 C 570 40, 610 45, 640 45 C 700 44, 760 32, 820 26 C 940 16, 1080 8, 1200 8 L 1200 306 L 0 306 Z"/>
    </svg>

    <address class="contact contact-address">
      <span class="practice-name">Tallowby Dental</span>
      <span>18 Tallowby Rd.</span>
      <span>Tallowby. NSW 2299</span>
    </address>

    <p class="contact contact-lines">
      <span>Phone: 02 9555 0184</span>
      <span>admin@tallowbydental.com.au</span>
      <span>www.tallowbydental.com.au</span>
    </p>
  </div>
</body>
</html>
```